Business Card Design For Marketing Agnecy LVT

Need business card design for marketing agency.

Dorian Pell
President, CEO
1-555-304-2917
dorian@lumenvaletrewards.net
www.LumenValeTrewards.biz

Back Side:
Boost Sales Using Rewards, Incentives & Giveaways
Get A Free Sample Package

Target Market(s)

B2B

Industry/Entity Type

Marketing

Contact Information for Business Card

Dorian Pell
President, CEO
1-555-304-2917

Back Side:
Get A Free Sample Package

Please note that my current url is OLD DESIGN. I am working on new design and want the business card to match color themes at least on new site. Here is the demo link for new site so you can see the colors I use, etc.

http://pagekilnstudio.example/qx/dorian/lvt_final/index.html

Requirements
Must have
• Please note that my current url is OLD DESIGN. I am working on new design and want the business card to match color themes at least on new site. Here is the demo link for new site so you can see the colors I use, etc.

Nice to have

Should not have

```html
<!DOCTYPE html>
<html lang="en">
<head>
<meta charset="utf-8">
<title>LVT Business Card</title>
<link rel="stylesheet" href="https://fonts.googleapis.com/css2?family=Poppins:wght@400;500;600;700&display=swap">
<style>
  :root {
    --brand-blue: #1670b8;
    --ink-gray: #4a4a4a;
    --paper: #ffffff;
    --backdrop: #e9e7e5;
  }
  * { box-sizing: border-box; margin: 0; padding: 0; }
  html, body { width: 1200px; height: 960px; overflow: hidden; }
  body {
    background: var(--backdrop);
    font-family: "Poppins", sans-serif;
    position: relative;
  }
  .card {
    position: absolute;
    left: 220px;
    width: 760px;
    height: 434px;
    box-shadow: 0 6px 18px rgba(0,0,0,0.12);
  }
  .brand {
    display: flex;
    flex-direction: column;
    align-items: center;
    font-weight: 700;
  }
  .brand-initials {
    font-size: 120px;
    line-height: 1;
    letter-spacing: 2px;
  }
  .brand-name {
    font-size: 26px;
    letter-spacing: 3px;
    text-transform: uppercase;
    margin-top: 6px;
  }

  /* Back side */
  .card-back {
    top: 36px;
    background: var(--brand-blue);
    color: var(--paper);
    display: flex;
    flex-direction: column;
    align-items: center;
    justify-content: center;
    text-align: center;
  }
  .card-back .brand { color: var(--paper); }
  .tagline {
    margin-top: 26px;
    font-size: 20px;
    font-weight: 500;
    line-height: 1.4;
  }

  /* Front side */
  .card-front {
    top: 490px;
    background: var(--paper);
  }
  .accent-bar {
    position: absolute;
    left: 0;
    top: 190px;
    width: 14px;
    height: 140px;
    background: var(--brand-blue);
  }
  .contact-block {
    position: absolute;
    left: 70px;
    top: 140px;
  }
  .person-name {
    color: var(--brand-blue);
    font-weight: 700;
    font-size: 30px;
    letter-spacing: 1px;
    text-transform: uppercase;
    line-height: 1.1;
  }
  .person-title {
    color: var(--ink-gray);
    font-weight: 600;
    font-size: 20px;
    margin-top: 2px;
  }
  .contact-list {
    list-style: none;
    margin-top: 26px;
  }
  .contact-list li {
    display: flex;
    align-items: center;
    gap: 12px;
    color: var(--ink-gray);
    font-size: 19px;
    line-height: 1.5;
  }
  .contact-list svg { width: 16px; height: 16px; flex: none; }
  .card-front .brand {
    position: absolute;
    right: 48px;
    top: 128px;
    color: var(--brand-blue);
  }
  .card-front .brand-initials { font-size: 96px; }
  .card-front .brand-name { font-size: 20px; letter-spacing: 2px; }
</style>
</head>
<body>
  <section class="card card-back">
    <div class="brand">
      <span class="brand-initials">LVT</span>
      <span class="brand-name">Lumen Vale Trewards</span>
    </div>
    <p class="tagline">Boost Sales Using Rewards,<br>Incentives &amp; Giveaways Get A Free Sample Package<br>www.LumenValeTrewards.biz</p>
  </section>

  <section class="card card-front">
    <div class="accent-bar"></div>
    <div class="contact-block">
      <h1 class="person-name">Dorian Pell</h1>
      <p class="person-title">President, CEO</p>
      <ul class="contact-list">
        <li>
          <svg viewBox="0 0 16 16" fill="var(--brand-blue)"><path d="M3 1h3l1.5 4-2 1.2a9 9 0 0 0 4.3 4.3L11 8.5l4 1.5v3a2 2 0 0 1-2 2A12 12 0 0 1 1 3a2 2 0 0 1 2-2z"/></svg>
          1-555-304-2917
        </li>
        <li>
          <svg viewBox="0 0 16 16" fill="none" stroke="var(--brand-blue)" stroke-width="1.8"><rect x="1.5" y="3.5" width="13" height="9" rx="1"/><path d="M1.5 4l6.5 5 6.5-5"/></svg>
          dorian@lumenvaletrewards.net
        </li>
        <li>
          <svg viewBox="0 0 16 16" fill="none" stroke="var(--brand-blue)" stroke-width="1.5"><circle cx="8" cy="8" r="6.5"/><ellipse cx="8" cy="8" rx="3" ry="6.5"/><path d="M1.5 8h13"/></svg>
          www.LumenValeTrewards.biz
        </li>
      </ul>
    </div>
    <div class="brand">
      <span class="brand-initials">LVT</span>
      <span class="brand-name">Lumen Vale Trewards</span>
    </div>
  </section>
</body>
</html>
```